landing page for web app project manager for Contractors/ craftsmen

create a great landing page that will attract customers to subscribe to our web app. Our web app is a project manager for trades (electricians,plumbers, cabinet makers, flooring installers and many more. It helps them organize their projects , tracking tasks, inventory and more. We want to communicate several important benefits and strategies.Our app is simple easy to use and has no unnecessary functions. It is designed for busy shops.
We want to point out that we see our app as a an inclusive tool that values and needs the feedback of our users so we can improve it continously.
similar apps are toolvane.net ( too complicated too many functions)

I uploaded 3 pdf's with landing page layouts that someone inhouse started
but the texts and wordings are bad and the overall look is not convincing enough.

Target Market(s)

web app for Trades/ craftsman/contractor businesses

Coding

Coded - Design and coding required

Number of Pages Required

1 page

Font styles to use
Sans Serif

Colors
9bcb3b
1b1b1b
5c5c5c
9d9d9d
f37122

Requirements
Must have
• please use the uploaded pdfs instead of images I like the sketched figures. They describe who can use the app and how it can turn chaos into order.Must haves on the landing page (not in order):
• excellent wording
• immediate understanding what it is , who can use it and what are the main benefits ( cost savings in the office due too better project management)
• breakdown of the functions,
• community approach: we want to communicate with our users how to improve it and what functions to add
• Free 14 day trial then rent per months or pay for the year at a discount, different packages available depending on nr of users
• Reviews
• animated video (comes later)
• sreenshots of functions
• and whatever you think that is crucial
Nice to have
• use these animations showing tradesmen and project management:
• https://media.pixoria-example.net/ca/search?filters%5Bcontent_type%3Aphoto%5D=1&filters%5Bcontent_type%3Aillustration%5D=1&filters%5Bcontent_type%3Azip_vector%5D=1&filters%5Bcontent_type%3Avideo%5D=1&filters%5Bcontent_type%3Atemplate%5D=1&filters%5Bcontent_type%3A3d%5D=1&filters%5Binclude_stock_enterprise%5D=0&filters%5Bis_editorial%5D=0&safe_search=1&search_page=2&acp=&aco=handwerker&limit=100&native_visual_search=&similar_content_id=557302841&serie_id=36205917

```html
<!DOCTYPE html>
<html lang="en">
<head>
<meta charset="utf-8">
<title>Benchwise – A Simple Project Manager</title>
<link href="https://fonts.googleapis.com/css2?family=Open+Sans:ital,wght@0,300;0,400;0,600;0,700;1,400&display=swap" rel="stylesheet">
<style>
:root{
  --green:#9bcb3b;
  --green-dark:#7fae25;
  --ink:#1b1b1b;
  --text:#5c5c5c;
  --muted:#9d9d9d;
  --accent:#f37122;
  --light:#f2f2f2;
  --card-head:#4a4a4a;
  --footer:#2b2b2b;
  --app-bar:#234d57;
  --line:#e3e3e3;
}
*{box-sizing:border-box;margin:0;padding:0}
html,body{width:1200px;height:4534px;overflow:hidden}
body{font-family:"Open Sans",Arial,sans-serif;color:var(--text);background:#fff;position:relative}
.abs{position:absolute}

/* header + hero */
.hero{left:0;top:0;width:1200px;height:575px;background:linear-gradient(135deg,#4a3423 0%,#2c2119 45%,#3d2d1e 70%,#1e1a16 100%)}
.hero-shade{left:0;top:0;width:1200px;height:575px;background:rgba(0,0,0,.35)}
.brand{display:flex;align-items:center;gap:12px;color:#fff;font-weight:700;font-size:32px;letter-spacing:.5px;line-height:1}
.brand-mark{width:32px;height:32px;background:var(--green)}
.brand-top{left:127px;top:22px}
.brand-foot{left:127px;top:4345px}
.nav{left:487px;top:30px;display:flex;align-items:center;gap:22px;font-size:12px;font-weight:600;color:#fff}
.nav .signup{background:#fff;color:var(--ink);padding:6px 14px;font-weight:700}
.nav-trial{display:flex;margin-left:12px}
.nav-trial .field{width:110px;height:30px;border:1px solid #fff;color:#fff;font-size:11px;padding:7px 10px;font-weight:400}
.nav-trial .go{height:30px;background:var(--green);color:var(--ink);padding:8px 12px;font-weight:700;font-size:11px}
.hero-title{left:0;width:1200px;top:196px;text-align:center;color:#fff;font-weight:300;font-size:44px}
.hero-title b{color:var(--green);font-weight:700}
.hero-sub{left:0;width:1200px;top:262px;text-align:center;color:#fff;font-size:17px}
.signup-form{left:332px;top:328px;display:flex}
.signup-form .field{width:398px;height:52px;background:#fff;display:flex;align-items:center;gap:10px;padding-left:22px;font-size:14px;color:var(--text)}
.signup-form .go{width:147px;height:52px;background:var(--green);color:#fff;font-weight:700;font-size:14px;display:flex;align-items:center;justify-content:center}
.hero-note{left:0;width:1200px;top:400px;text-align:center;color:#fff;font-size:14px}
.trial-band{left:0;top:540px;width:1200px;height:35px;background:var(--green-dark);color:#fff;font-size:13px;font-weight:700;text-align:center;line-height:35px;letter-spacing:.3px}

/* trades */
.trades-title{left:0;width:1200px;top:632px;text-align:center;color:var(--green);font-weight:700;font-size:27px;line-height:38px;text-transform:uppercase}
.trade-list{list-style:none;font-size:12.5px;color:var(--text);line-height:21.5px}
.trade-list li{display:flex;align-items:center;gap:8px}
.devices{left:790px;top:750px;width:300px;height:250px;background:linear-gradient(160deg,#f5f5f5,#dcdcdc);border-radius:6px}

/* benefits */
.intro{left:0;width:1200px;top:1088px;text-align:center;font-size:22px;line-height:32px;color:var(--ink);font-weight:300}
.intro-small{left:0;width:1200px;top:1168px;text-align:center;font-size:14px;color:var(--ink)}
.benefits{left:100px;top:1238px;width:1000px;display:flex}
.benefit{width:166.6px;text-align:center;padding:0 12px;border-left:1px solid var(--line)}
.benefit:first-child{border-left:none}
.benefit svg{width:40px;height:40px;display:block;margin:0 auto 22px}
.benefit h3{font-size:14px;font-weight:600;color:var(--ink);margin-bottom:10px;white-space:nowrap}
.benefit p{font-size:11.5px;line-height:15px;color:var(--text)}

/* welcome */
.welcome{left:0;top:1451px;width:1200px;height:408px;background:var(--light)}
.welcome-title{left:127px;top:1530px;font-size:23px;font-weight:400;color:var(--ink)}
.welcome-copy{left:127px;top:1572px;width:360px;font-size:12px;line-height:16.5px;color:var(--text)}
.btn-small{background:var(--green);color:#fff;font-size:11px;font-weight:700;padding:8px 18px;display:inline-block}
.video{left:526px;top:1481px;width:541px;height:324px;background:linear-gradient(135deg,#8c8f8a,#b6b3a6 40%,#6f7470 100%)}
.play{left:763px;top:1610px;width:66px;height:66px}

/* feature showcase */
.showcase-title{left:0;width:1200px;top:1902px;text-align:center;font-size:22px;color:var(--ink);font-weight:300}
.showcase-title b{color:var(--green-dark);font-weight:700}
.step-no{font-size:66px;font-weight:300;color:#d5d5d5;line-height:1}
.step h3{font-size:17px;font-weight:400;color:var(--ink);margin:18px 0 12px}
.step p{font-size:13px;line-height:19px;color:var(--text)}
.step.center{text-align:center;width:290px}
.step.left{text-align:left;width:300px}

.app{background:#fff;box-shadow:0 14px 40px rgba(0,0,0,.16);border:1px solid #ddd;overflow:hidden}
.app-bar{height:30px;background:var(--app-bar)}
.app-body{display:flex;height:calc(100% - 30px)}
.app-side{width:92px;border-right:1px solid var(--line);padding-top:12px;font-size:10px;color:var(--text)}
.app-side div{padding:6px 12px}
.app-side .on{color:var(--app-bar);font-weight:700}
.app-main{flex:1;padding:14px 18px}
.app-main h4{font-size:16px;color:#c0392b;font-weight:600;margin-bottom:12px}
.app-main table{width:100%;border-collapse:collapse;font-size:10px;color:var(--text)}
.app-main th{text-align:left;font-weight:700;color:var(--ink);border-bottom:2px solid var(--line);padding:6px 4px}
.app-main td{border-bottom:1px solid var(--line);padding:9px 4px}
.app-main td.link{color:#2a8bb8}

/* packages */
.packages{left:0;top:3531px;width:1200px;height:520px;background:var(--light)}
.packages-title{left:0;width:1200px;top:3568px;text-align:center;font-size:20px;font-weight:400;color:var(--ink)}
.plans{left:133px;top:3649px;display:flex;gap:24px}
.plan{width:215px;background:#fff;text-align:center}
.plan-head{height:100px;background:var(--card-head);color:#fff;padding-top:20px}
.plan.featured .plan-head{background:var(--green)}
.plan-name{font-size:13px;font-weight:600;letter-spacing:.5px}
.plan-price{font-size:30px;font-weight:700;margin-top:4px}
.plan-price sup{font-size:14px}
.plan ul{list-style:none;font-size:12px;color:var(--text)}
.plan li{border-bottom:1px solid var(--line);padding:8px 0;margin:0 18px}
.plan .btn-small{margin:16px 0 20px}

/* review */
.reviews-title{left:0;width:1200px;top:4068px;text-align:center;font-size:20px;font-weight:400;color:var(--ink)}
.reviewer{left:136px;top:4135px;width:137px;height:137px;border-radius:50%;background:linear-gradient(160deg,#c9d3dc,#8fa2b3);border:4px solid #fff;box-shadow:0 0 0 1px var(--line)}
.quote-mark{font-size:60px;color:#cfcfcf;font-weight:700;line-height:1}
.review-text{left:332px;top:4148px;width:740px;font-size:12.5px;line-height:18px;color:var(--text)}
.review-by{left:332px;top:4220px;font-size:14px;color:var(--text)}
.review-by b{color:var(--green-dark);font-weight:400}
.dots{left:573px;top:4252px;display:flex;gap:8px}
.dots span{width:9px;height:9px;border-radius:50%;background:#cfcfcf}
.dots span.on{background:var(--green-dark)}

/* footer */
.footer{left:0;top:4293px;width:1200px;height:241px;background:var(--footer)}
.follow{left:513px;top:4350px;display:flex;align-items:center;gap:10px;font-size:12px;color:#ccc}
.follow span.dot{width:26px;height:26px;border-radius:50%;background:#2f76c0}
.foot-links{right:127px;top:4347px;text-align:right;font-size:12px;color:#ddd;line-height:22px}
.foot-links small{font-size:11px;color:var(--muted)}
</style>
</head>
<body>

<!-- header / hero -->
<div class="abs hero" role="img" aria-label="Photo of craftsman hand tools laid out on a workbench"></div>
<div class="abs hero-shade"></div>
<div class="abs brand brand-top"><span class="brand-mark"></span>Benchwise</div>
<nav class="abs nav">
  <span>HOME</span><span>ABOUT</span><span>SERVICES</span><span>CONTACT</span>
  <span class="signup">SIGNUP</span>
  <span class="nav-trial"><span class="field">✉ E-mail Id</span><span class="go">FREE TRIAL</span></span>
</nav>
<h1 class="abs hero-title">A Simple <b>Project</b> Manager</h1>
<p class="abs hero-sub">Build for crafts and tradesman businesses</p>
<div class="abs signup-form">
  <div class="field"><svg width="14" height="11" viewBox="0 0 14 11"><rect x="0.5" y="0.5" width="13" height="10" fill="none" stroke="#5c5c5c"/><path d="M1 1l6 5 6-5" fill="none" stroke="#5c5c5c"/></svg>Enter Your Email Address</div>
  <div class="go">GET STARTED</div>
</div>
<p class="abs hero-note">Create your first project in seconds. Currently free to try, no credit card required</p>
<div class="abs trial-band">FREE 14 DAY TRIAL THEN RENT PER MONTHS OR PAY FOR THE YEAR AT A DISCOUNT</div>

<!-- trades -->
<h2 class="abs trades-title">Benchwise is built for crafts- and tradesman<br>businesses with 1-10 employees.</h2>
<svg width="0" height="0" style="position:absolute"><defs><symbol id="tick" viewBox="0 0 12 12"><path d="M1.5 6.5l3 3 6-7" fill="none" stroke="#7fae25" stroke-width="2"/></symbol></defs></svg>
<ul class="abs trade-list" style="left:127px;top:800px">
  <li><svg width="11" height="11"><use href="#tick"/></svg>Electricians</li>
  <li><svg width="11" height="11"><use href="#tick"/></svg>Plumbers</li>
  <li><svg width="11" height="11"><use href="#tick"/></svg>Mechanics</li>
  <li><svg width="11" height="11"><use href="#tick"/></svg>Flooring installers</li>
  <li><svg width="11" height="11"><use href="#tick"/></svg>contractors</li>
  <li><svg width="11" height="11"><use href="#tick"/></svg>Blacksmithes</li>
  <li><svg width="11" height="11"><use href="#tick"/></svg>Pest Control</li>
  <li><svg width="11" height="11"><use href="#tick"/></svg>Roofers</li>
</ul>
<ul class="abs trade-list" style="left:308px;top:800px">
  <li><svg width="11" height="11"><use href="#tick"/></svg>Doors and window companies</li>
  <li><svg width="11" height="11"><use href="#tick"/></svg>Landscapers</li>
  <li><svg width="11" height="11"><use href="#tick"/></svg>Finishing Shops</li>
  <li><svg width="11" height="11"><use href="#tick"/></svg>Woodworkers</li>
  <li><svg width="11" height="11"><use href="#tick"/></svg>Maintenance and repairs</li>
  <li><svg width="11" height="11"><use href="#tick"/></svg>Riggers</li>
  <li><svg width="11" height="11"><use href="#tick"/></svg>Machinists</li>
</ul>
<ul class="abs trade-list" style="left:544px;top:800px">
  <li><svg width="11" height="11"><use href="#tick"/></svg>Welders</li>
  <li><svg width="11" height="11"><use href="#tick"/></svg>Cabinetmakers</li>
  <li><svg width="11" height="11"><use href="#tick"/></svg>Carpenters</li>
  <li><svg width="11" height="11"><use href="#tick"/></svg>Tile and marble setters</li>
  <li><svg width="11" height="11"><use href="#tick"/></svg>Painters</li>
  <li><svg width="11" height="11"><use href="#tick"/></svg>Heating and air conditioning installers</li>
  <li><svg width="11" height="11"><use href="#tick"/></svg>Others</li>
</ul>
<div class="abs devices" role="img" aria-label="Desktop monitor and tablet showing the app start screen"></div>

<!-- benefits -->
<p class="abs intro">We know first hand how hard it can be to<br>manage a busy craftsmen business.</p>
<p class="abs intro-small">Here is how Benchwise can help</p>
<div class="abs benefits">
  <div class="benefit">
    <svg viewBox="0 0 44 44"><circle cx="22" cy="22" r="9" fill="none" stroke="#7fae25" stroke-width="6" stroke-dasharray="5 2.1"/><circle cx="22" cy="22" r="4" fill="#7fae25"/></svg>
    <h3>Easy Setup</h3><p>Create new projects<br>in seconds</p>
  </div>
  <div class="benefit">
    <svg viewBox="0 0 44 44"><rect x="10" y="6" width="24" height="32" fill="none" stroke="#7fae25" stroke-width="3"/><path d="M15 15h14M15 22h14M15 29h10" stroke="#7fae25" stroke-width="2.5"/></svg>
    <h3>Task Lists</h3><p>Split projects into tasks and tick them off one by one</p>
  </div>
  <div class="benefit">
    <svg viewBox="0 0 44 44"><circle cx="22" cy="22" r="15" fill="none" stroke="#7fae25" stroke-width="3"/><path d="M22 13v10l7 4" fill="none" stroke="#7fae25" stroke-width="3"/></svg>
    <h3>Simple Scheduling</h3><p>What and when it's due, who's responsible</p>
  </div>
  <div class="benefit">
    <svg viewBox="0 0 44 44"><circle cx="13" cy="10" r="4" fill="#7fae25"/><path d="M8 38V18h10v20" fill="#7fae25"/><rect x="21" y="26" width="11" height="12" fill="#7fae25"/><rect x="25" y="14" width="11" height="11" fill="#7fae25"/></svg>
    <h3>Inventory Management</h3><p>Never forget to reorder<br>in time</p>
  </div>
  <div class="benefit">
    <svg viewBox="0 0 44 44"><rect x="7" y="10" width="30" height="27" fill="none" stroke="#7fae25" stroke-width="3"/><path d="M7 17h30M15 6v7M29 6v7" stroke="#7fae25" stroke-width="3"/><rect x="13" y="22" width="5" height="4" fill="#7fae25"/><rect x="21" y="22" width="5" height="4" fill="#7fae25"/><rect x="13" y="29" width="5" height="4" fill="#7fae25"/></svg>
    <h3>Calendar</h3><p>Have an eye on all<br>upcoming dates</p>
  </div>
  <div class="benefit">
    <svg viewBox="0 0 44 44"><ellipse cx="22" cy="10" rx="13" ry="5" fill="#7fae25"/><path d="M9 15c0 3 6 5 13 5s13-2 13-5v6c0 3-6 5-13 5S9 24 9 21zM9 26c0 3 6 5 13 5s13-2 13-5v6c0 3-6 5-13 5S9 35 9 32z" fill="#7fae25"/></svg>
    <h3>Web-based</h3><p>World wide access, from any device that runs a modern browser</p>
  </div>
</div>

<!-- welcome -->
<div class="abs welcome"></div>
<h2 class="abs welcome-title">Welcome to our site</h2>
<p class="abs welcome-copy">Lorem ipsum dolor sit amet, consectetur adipiscing elit. Suspendisse convallis lobortis ante, sit amet aliquam ligula pharetra ac. Mauris consectetur hendrerit risus vitae efficitur. Mauris ut nunc et lorem sollicitudin accumsan in interdum felis. Aliquam erat volutpat. Nunc et consequat nulla. Morbi scelerisque.</p>
<span class="abs btn-small" style="left:127px;top:1716px">READ MORE</span>
<div class="abs video" role="img" aria-label="Video still of a tradesman in a hard hat and safety vest on a work site"></div>
<svg class="abs play" viewBox="0 0 66 66"><circle cx="33" cy="33" r="33" fill="#fff"/><path d="M26 20l22 13-22 13z" fill="#5c5c5c"/></svg>

<!-- feature showcase -->
<h2 class="abs showcase-title">Make managing <b>your projects</b> simple and fun again</h2>

<div class="abs step center" style="left:345px;top:2070px">
  <div class="step-no">01</div>
  <h3>The Project Overview</h3>
  <p>Have all your Projects organized in one place. See exactly what is done, what is due, where you're at and who's responsible.</p>
</div>
<div class="abs app" style="left:665px;top:2010px;width:560px;height:390px">
  <div class="app-bar"></div>
  <div class="app-body">
    <div class="app-side"><div class="on">Projects</div><div>Tasks</div><div>Inventory</div><div>Calendar</div><div>Team</div></div>
    <div class="app-main"><h4>Projects</h4>
      <table>
        <tr><th>Project</th><th>Client</th><th>Status</th><th>Due</th></tr>
        <tr><td>Kitchen refit</td><td>Hale</td><td>Active</td><td class="link">09/12</td></tr>
        <tr><td>Deck repair</td><td>Moss</td><td>Open</td><td class="link">09/15</td></tr>
        <tr><td>Bath tiling</td><td>Ortiz</td><td>Active</td><td class="link">09/21</td></tr>
        <tr><td>Roof patch</td><td>Lund</td><td>Done</td><td class="link">09/28</td></tr>
        <tr><td>Shop wiring</td><td>Prior</td><td>Open</td><td class="link">10/02</td></tr>
        <tr><td>Fence build</td><td>Vance</td><td>Active</td><td class="link">10/09</td></tr>
      </table>
    </div>
  </div>
</div>

<div class="abs app" style="left:-20px;top:2495px;width:600px;height:390px">
  <div class="app-bar"></div>
  <div class="app-body">
    <div class="app-side"><div>Projects</div><div class="on">Tasks</div><div>Inventory</div><div>Calendar</div><div>Team</div></div>
    <div class="app-main"><h4>Tasks</h4>
      <table>
        <tr><th>Task</th><th>Assigned</th><th>Status</th><th>Due</th></tr>
        <tr><td>Cut panels</td><td>Ray</td><td>Open</td><td class="link">09/12</td></tr>
        <tr><td>Order tile</td><td>Sam</td><td>Done</td><td class="link">09/13</td></tr>
        <tr><td>Fit hinges</td><td>Ray</td><td>Open</td><td class="link">09/14</td></tr>
        <tr><td>Run cable</td><td>Lee</td><td>Active</td><td class="link">09/16</td></tr>
        <tr><td>Seal joints</td><td>Sam</td><td>Open</td><td class="link">09/18</td></tr>
        <tr><td>Final check</td><td>Lee</td><td>Open</td><td class="link">09/20</td></tr>
      </table>
    </div>
  </div>
</div>
<div class="abs step left" style="left:640px;top:2585px">
  <div class="step-no">02</div>
  <h3>The Task List</h3>
  <p>Split projects into tasks, delegate employees, track the progress and tick them off one by one.</p>
</div>

<div class="abs step center" style="left:345px;top:3100px">
  <div class="step-no">03</div>
  <h3>The Inventory Section</h3>
  <p>Add new inventory items, track the amount, add vendors and know when to reorder.</p>
</div>
<div class="abs app" style="left:665px;top:3005px;width:560px;height:390px">
  <div class="app-bar"></div>
  <div class="app-body">
    <div class="app-side"><div>Projects</div><div>Tasks</div><div class="on">Inventory</div><div>Calendar</div><div>Team</div></div>
    <div class="app-main"><h4>Inventory Items</h4>
      <table>
        <tr><th>Item</th><th>Qty</th><th>Vendor</th><th>Reorder</th></tr>
        <tr><td>Copper pipe</td><td>40</td><td>Marlow</td><td class="link">No</td></tr>
        <tr><td>Wood screws</td><td>900</td><td>Fastco</td><td class="link">No</td></tr>
        <tr><td>Drywall sheet</td><td>12</td><td>Ridge</td><td class="link">Yes</td></tr>
        <tr><td>PVC elbow</td><td>65</td><td>Marlow</td><td class="link">No</td></tr>
        <tr><td>Wire spool</td><td>3</td><td>Voltline</td><td class="link">Yes</td></tr>
        <tr><td>Tile grout</td><td>18</td><td>Ridge</td><td class="link">No</td></tr>
      </table>
    </div>
  </div>
</div>

<!-- packages -->
<div class="abs packages"></div>
<h2 class="abs packages-title">Packages</h2>
<div class="abs plans">
  <div class="plan">
    <div class="plan-head"><div class="plan-name">STARTER</div><div class="plan-price">$59.<sup>99</sup></div></div>
    <ul><li>Lorem Ipsum is simp</li><li>It is a long establishe</li><li>There are many variation</li><li>Various versions hav</li><li>Remaining Essentially</li></ul>
    <span class="btn-small">CHOOSE PACKAGE</span>
  </div>
  <div class="plan">
    <div class="plan-head"><div class="plan-name">STANDARD</div><div class="plan-price">$69.<sup>99</sup></div></div>
    <ul><li>Lorem Ipsum is simp</li><li>It is a long establishe</li><li>There are many variation</li><li>Various versions hav</li><li>Remaining Essentially</li></ul>
    <span class="btn-small">CHOOSE PACKAGE</span>
  </div>
  <div class="plan featured">
    <div class="plan-head"><div class="plan-name">ENHANCED</div><div class="plan-price">$89.<sup>99</sup></div></div>
    <ul><li>Lorem Ipsum is simp</li><li>It is a long establishe</li><li>There are many variation</li><li>Various versions hav</li><li>Remaining Essentially</li></ul>
    <span class="btn-small">CHOOSE PACKAGE</span>
  </div>
  <div class="plan">
    <div class="plan-head"><div class="plan-name">PREMIUM</div><div class="plan-price">$109.<sup>99</sup></div></div>
    <ul><li>Lorem Ipsum is simp</li><li>It is a long establishe</li><li>There are many variation</li><li>Various versions hav</li><li>Remaining Essentially</li></ul>
    <span class="btn-small">CHOOSE PACKAGE</span>
  </div>
</div>

<!-- review -->
<h2 class="abs reviews-title">Customer Reviews</h2>
<div class="abs reviewer" role="img" aria-label="Portrait photo of the reviewing company founder"></div>
<div class="abs quote-mark" style="left:292px;top:4135px">“</div>
<p class="abs review-text">But I must explain to you how all this mistaken idea of denouncing pleasure and praising pain was born and I will give you a complete account of the system, and expound the actual teachings of the great explorer of the truth, the master-builder of human happiness. No one rejects, dislikes, or avoids pleasure itself, because it is pleasure.</p>
<div class="abs quote-mark" style="left:1078px;top:4185px">”</div>
<p class="abs review-by"><b>Founder Benchwise</b> - Oakline Joinery, Built to Last</p>
<div class="abs dots"><span class="on"></span><span class="on"></span><span></span></div>

<!-- footer -->
<div class="abs footer"></div>
<div class="abs brand brand-foot"><span class="brand-mark"></span>Benchwise</div>
<div class="abs follow">Follow us On :<span class="dot"></span><span class="dot"></span><span class="dot"></span></div>
<div class="abs foot-links">About &nbsp;|&nbsp; Contact &nbsp;|&nbsp; Legal &nbsp;|&nbsp; Login<br><small>Copyright © 2018 All Rights Reserved</small></div>

</body>
</html>
```